Craft brewery website - 7 Harbors Brewery

Looking for a simple site similar to fennwaldbrew.com or tallridgeales.com with the following features:
- incorporates existing logo (file attached)
- has a consistent look and feel throughout the site that works in harmony with the logo. Please suggest a cool font to use!
- incorporates all or some of the attached images
- has the following tabs/pages: home, our story, brews, blog, contact.
- has some sort of prominent image/design under the top menu bar that can be updated with content - so a placeholder for text. Please use this text on home page: "we brew up our passion for honest ingredients, our curiosity for different cultures, and social and environmental consciousness into characteristic beers." And "Beers with a Twist for the good of the world, for the fun of the party"
- has a scrolling set of images under main section that will list beers. Please create five placeholders for beers: Weizenbock, Copper Lantern, Stout, Saison, Rusty Marlow

Brewery

1 page

• Looking for a simple site similar to fennwaldbrew.com with the following features:
• - incorporates existing logo (file attached)
• - has a consistent look and feel throughout the site that works in harmony with the logo. Please suggest a cool font to use!
• - incorporates all or some of the attached images
• - has the following tabs/pages: home, our story, brews, blog, contact.
• - has some sort of prominent image/design under the top menu bar that can be updated with content - so a placeholder for text. Please use this text on home page: "we brew up our passion for honest ingredients, our curiosity for different cultures, and social and environmental consciousness into characteristic beers." And "Beers with a Twist for the good of the world, for the fun of the party"
• - has a scrolling set of images under main section that will list beers. Please create five placeholders for beers: Weizenbock, Copper Lantern, Stout, Saison, Rusty Marlow

```html
<!DOCTYPE html>
<html lang="en">
<head>
<meta charset="utf-8">
<title>7 Harbors Brewery</title>
<link href="https://fonts.googleapis.com/css2?family=Oswald:wght@400;500;600&family=Open+Sans:wght@400;600;700&display=swap" rel="stylesheet">
<style>
:root{
  --gold:#c58c2b;
  --gold-dark:#a87320;
  --cream:#f2efe8;
  --paper:#f7f5f0;
  --ink:#2b2b2b;
  --muted:#666;
  --footer:#1f1f1f;
  --footer-text:#d8d8d8;
  --hero-a:#7a6546;
  --hero-b:#4f4230;
}
*{box-sizing:border-box;margin:0;padding:0}
html,body{width:1200px;height:4009px;overflow:hidden}
body{background:var(--cream);font-family:"Open Sans",sans-serif;color:var(--ink);position:relative}
h2.section-title{font-family:"Oswald",sans-serif;font-weight:500;color:var(--gold);font-size:32px;letter-spacing:.5px;text-transform:uppercase}
.btn{display:inline-block;background:var(--gold);color:#fff;font-family:"Oswald",sans-serif;font-size:17px;text-transform:uppercase;padding:0 18px;line-height:50px;text-decoration:none}
.rule{position:absolute;left:0;width:1200px;height:6px;background:var(--gold)}
.rule::after{content:"";position:absolute;left:0;right:0;top:8px;height:2px;background:var(--gold);opacity:.45}
p{font-size:15px;line-height:1.75}

/* header */
.site-header{position:absolute;top:0;left:0;width:1200px;height:171px;background:var(--paper)}
.topbar{position:absolute;right:80px;top:36px;font-size:15px;font-weight:600;color:#444;display:flex;gap:14px;align-items:center}
.topbar svg{width:15px;height:15px;fill:#444;vertical-align:-2px;margin-right:6px}
.main-nav{position:absolute;right:80px;top:100px;display:flex;gap:28px}
.main-nav a{font-family:"Oswald",sans-serif;font-size:25px;color:var(--gold);text-decoration:none;text-transform:uppercase}
.brand{position:absolute;left:94px;top:12px;width:204px;height:204px;border-radius:50%;background:var(--paper);border:6px solid var(--gold);display:flex;align-items:center;justify-content:center;text-align:center;z-index:3}
.brand span{font-family:"Oswald",sans-serif;font-weight:500;color:var(--gold);font-size:27px;line-height:1.15;text-transform:uppercase}

/* hero */
.hero{position:absolute;top:171px;left:0;width:1200px;height:545px;background:linear-gradient(90deg,var(--hero-b),var(--hero-a) 55%,#8b7a63)}
.hero-art{position:absolute;right:70px;top:0;width:380px;height:545px;background:linear-gradient(180deg,#3f3a3a,#6a5a6e 50%,#9a4a3a);opacity:.75}
.hero-copy{position:absolute;left:99px;top:160px;color:#fff}
.hero-copy .kicker{font-family:"Oswald",sans-serif;font-size:27px;text-transform:uppercase}
.hero-copy h1{font-family:"Oswald",sans-serif;font-weight:500;color:var(--gold);font-size:50px;text-transform:uppercase;line-height:1.15;margin-top:6px}
.hero-copy p{font-size:15px;font-weight:600;width:430px;margin-top:12px;line-height:1.6}
.hero-copy .btn{margin-top:30px}
.hero-arrow{position:absolute;top:248px;width:30px;height:60px}
.hero-arrow path{fill:none;stroke:#fff;stroke-width:2.5;opacity:.8}

/* welcome */
.welcome{position:absolute;top:722px;left:0;width:1200px;text-align:center}
.welcome h2{margin-top:46px;font-size:36px}
.welcome p{width:1000px;margin:30px auto 0;color:#444}
.beer-row{position:absolute;top:1040px;left:70px;width:1060px;display:flex}
.beer{width:212px;text-align:center;position:relative}
.beer + .beer::before{content:"";position:absolute;left:0;top:10px;width:4px;height:210px;background:var(--gold)}
.beer-photo{width:160px;height:160px;border-radius:50%;margin:0 auto;border:4px solid #d9cbb4;background:radial-gradient(circle,#a0452c,#5a2a1c 55%,#8f8072)}
.beer:nth-child(2) .beer-photo{background:radial-gradient(circle,#6a2418,#2a1a14 55%,#8f8072)}
.beer:nth-child(3) .beer-photo{background:radial-gradient(circle,#2a1c14,#4e3a26 55%,#9a8c7c)}
.beer:nth-child(4) .beer-photo{background:radial-gradient(circle,#c88b35,#7a4f22 55%,#8f8072)}
.beer:nth-child(5) .beer-photo{background:radial-gradient(circle,#3a2a20,#6a5444 55%,#9a8c7c)}
.beer h3{font-family:"Oswald",sans-serif;font-weight:500;color:var(--gold);font-size:21px;text-transform:uppercase;margin-top:26px}

/* story + blog */
.story{position:absolute;top:1420px;left:99px;width:450px}
.framed{border:5px solid var(--gold);padding:10px;background:var(--paper)}
.story .framed{margin-top:42px;height:300px}
.story-photo{width:100%;height:100%;background:linear-gradient(135deg,#b9b3a8,#e6e1d8 45%,#8f8aa0 80%,#c0403a)}
.story p{font-size:13px;color:#555;margin-top:16px;line-height:1.7}
.more{font-family:"Oswald",sans-serif;font-size:13px;color:var(--gold);text-transform:uppercase;display:block;margin-top:8px;letter-spacing:.5px}
.blog{position:absolute;top:1420px;left:601px;width:500px}
.post{display:flex;gap:22px;margin-top:44px}
.post + .post{margin-top:50px}
.post .framed{width:155px;height:128px;padding:6px;flex:none}
.post-photo{width:100%;height:100%;background:linear-gradient(135deg,#cfc9be,#6b6a7c 55%,#3b5aa6)}
.post h4{font-size:14px;font-weight:600;color:#333}
.post .meta{font-size:12px;color:#888;margin-top:10px;font-style:italic;display:flex;gap:18px}
.post p{font-size:13px;color:#666;margin-top:10px;line-height:1.6}

/* brews */
.brews{position:absolute;top:1957px;left:0;width:1200px;text-align:center}
.brews h2{margin-top:55px;font-size:36px}
.brews p{width:1000px;margin:26px auto 0;font-weight:600;font-size:15px}
.brews-photo{position:absolute;top:2190px;left:290px;width:620px;height:205px;border-radius:6px;background:linear-gradient(90deg,#6a1d14,#c8661e 20%,#2c1a12 38%,#d06a14 58%,#b0571c 78%,#e08a2a);opacity:.85}

/* events */
.events{position:absolute;top:2575px;left:99px;width:500px}
.events p.lead{font-size:19px;line-height:1.6;margin-top:22px;width:440px}
.events .btn{margin-top:28px;height:54px;line-height:54px}
.hours{margin-top:38px;font-family:"Oswald",sans-serif;color:var(--gold);font-size:19px;line-height:1.85;text-transform:uppercase}
.events-art{position:absolute;top:2540px;left:601px;width:430px;height:455px;background:linear-gradient(160deg,#e8e4dc,#7a86c4 35%,#2a2a2a 60%,#c0462e 85%,#e8e4dc);opacity:.8;border-radius:6px}

/* shop */
.shop-art{position:absolute;top:3087px;left:107px;width:400px;height:390px;background:linear-gradient(135deg,#c9c6cf,#2b2b2b 45%,#a43a2a 75%,#e8e4dc);opacity:.8;border-radius:6px}
.shop{position:absolute;top:3115px;left:570px;width:540px}
.shop p{font-weight:600;font-size:14px;margin-top:18px;line-height:1.7}
.products{display:flex;gap:27px;margin-top:30px}
.products .framed{width:148px;height:140px;padding:8px}
.product{width:100%;height:100%}
.product.cap{background:radial-gradient(circle,#2f4f7a 35%,var(--paper) 37%)}
.product.tank{background:radial-gradient(ellipse 30% 42%,#2f56b0 90%,var(--paper) 92%)}
.product.growler{background:radial-gradient(ellipse 22% 42%,#7a4a26 90%,var(--paper) 92%)}
.shop .btn{margin-top:36px;height:54px;line-height:54px}

/* footer */
.site-footer{position:absolute;top:3560px;left:0;width:1200px;height:449px;background:var(--footer);color:var(--footer-text)}
.footer-col{position:absolute;top:70px}
.footer-col h5{font-family:"Oswald",sans-serif;font-weight:500;color:var(--gold);font-size:23px;text-transform:uppercase}
.footer-col p{font-size:13px;line-height:1.75;margin-top:22px;width:300px}
.links{list-style:none;margin-top:22px}
.links li{font-size:14px;line-height:2.3;font-weight:600}
.links li::before{content:"›";margin-right:8px}
.contact-item{display:flex;gap:14px;margin-top:24px;font-size:12px;line-height:1.55}
.contact-item b{font-size:13px;display:block}
.ico{flex:none;width:32px;height:32px;border:2px solid var(--gold);border-radius:50%;display:flex;align-items:center;justify-content:center}
.ico svg{width:14px;height:14px;fill:var(--gold)}
.newsletter input{display:block;margin-top:22px;width:226px;height:34px;background:transparent;border:1px solid #bbb;color:#ddd;padding:0 10px;font-size:12px;font-family:inherit}
.newsletter .btn{margin-top:16px;font-size:14px;line-height:32px;padding:0 14px}
.footer-rule{position:absolute;left:99px;right:99px;top:359px;height:2px;background:var(--gold)}
.copyright{position:absolute;left:99px;top:394px;font-size:14px;font-weight:600}
.social{position:absolute;right:99px;top:384px;display:flex;gap:10px}
.social span{width:40px;height:40px;border:2px solid #ddd;border-radius:50%}
</style>
</head>
<body>

<header class="site-header">
  <div class="brand"><span>7 Harbors<br>Brewery</span></div>
  <div class="topbar">
    <span><svg viewBox="0 0 16 16"><path d="M1 3h14v10H1z M1 3l7 6 7-6" fill="none" stroke="#444" stroke-width="1.6"/></svg>BUILDING 1, ALDER ST 123, HIGH ROAD</span>
    <span>•</span>
    <span><svg viewBox="0 0 16 16"><path d="M3 1l3 0 1 4-2 1c1 2 3 4 5 5l1-2 4 1v3c0 1-1 2-2 2C7 15 1 9 1 3c0-1 1-2 2-2z"/></svg>180 047 3918</span>
  </div>
  <nav class="main-nav">
    <a href="#">Home</a><a href="#">Our Story</a><a href="#">Brews</a><a href="#">Blog</a><a href="#">Events</a><a href="#">Shop</a><a href="#">Contact</a>
  </nav>
</header>

<section class="hero">
  <div class="hero-art" role="img" aria-label="Street mural of a seated figure holding a blue flag"></div>
  <svg class="hero-arrow" style="left:26px" viewBox="0 0 30 60"><path d="M26 4L4 30l22 26"/></svg>
  <svg class="hero-arrow" style="right:26px" viewBox="0 0 30 60"><path d="M4 4l22 26L4 56"/></svg>
  <div class="hero-copy">
    <div class="kicker">We brew up our passion</div>
    <h1>7 Harbors Brewery</h1>
    <p>We brew up our passion for honest ingredients, our curiosity for different cultures.</p>
    <a class="btn" href="#">Contact here!</a>
  </div>
</section>
<div class="rule" style="top:713px"></div>

<section class="welcome">
  <h2 class="section-title">Welcome to 7 Harbors Brewery</h2>
  <p>we brew up our passion for honest ingredients, our curiosity for different cultures, and social and environmental consciousness into characteristic beers." And "Beers with a Twist for the good of the world, for the fun of the party"</p>
</section>
<div class="beer-row">
  <div class="beer"><div class="beer-photo" role="img" aria-label="Weizenbock bottles"></div><h3>Weizenbock</h3></div>
  <div class="beer"><div class="beer-photo" role="img" aria-label="Copper Lantern bottles"></div><h3>Copper Lantern</h3></div>
  <div class="beer"><div class="beer-photo" role="img" aria-label="Stout bottle and glass"></div><h3>Stout</h3></div>
  <div class="beer"><div class="beer-photo" role="img" aria-label="Saison bottles"></div><h3>Saison</h3></div>
  <div class="beer"><div class="beer-photo" role="img" aria-label="Rusty Marlow bottle"></div><h3>Rusty Marlow</h3></div>
</div>
<div class="rule" style="top:1366px"></div>

<section class="story">
  <h2 class="section-title">Our Story</h2>
  <div class="framed"><div class="story-photo" role="img" aria-label="Wall mural with an arrow and shield"></div></div>
  <p>Sed ut perspiciatis unde omnis iste natus error sit voluptatem accusan tium dolore mque quasi architecto beatae vitae.</p>
  <a class="more" href="#">Read more &gt;&gt;</a>
</section>
<section class="blog">
  <h2 class="section-title">Latest Blog</h2>
  <article class="post">
    <div class="framed"><div class="post-photo" role="img" aria-label="Mural of a seated figure"></div></div>
    <div><h4>Neque porro quisquam est qui dolorem ipsum</h4><div class="meta"><span>2nd, 3rd Jan 2017</span><span>NORA VELL</span></div><p>Sed ut perspiciatis unde omnis iste natus error sit voluptatem accusantium dolore mque.</p></div>
  </article>
  <article class="post">
    <div class="framed"><div class="post-photo" role="img" aria-label="Mural of a seated figure"></div></div>
    <div><h4>Neque porro quisquam est qui dolorem ipsum</h4><div class="meta"><span>2nd, 3rd Jan 2017</span><span>NORA VELL</span></div><p>Sed ut perspiciatis unde omnis iste natus error sit voluptatem accusantium dolore mque.</p></div>
  </article>
  <a class="more" href="#" style="margin-top:22px">View more &gt;&gt;</a>
</section>
<div class="rule" style="top:1948px"></div>

<section class="brews">
  <h2 class="section-title">Our Brews</h2>
  <p>We brew up our passion for honest ingredients, our curiosity for different cultures, and social and environmental consciousness into characteristic beers." And "Beers with a Twist for the good of the world, for the fun of the party"</p>
</section>
<div class="brews-photo" role="img" aria-label="Photo of a row of six glasses of different beers"></div>
<div class="rule" style="top:2488px"></div>

<section class="events">
  <h2 class="section-title">Our Events</h2>
  <p class="lead">Click the button below to view and participate in upcoming events.</p>
  <a class="btn" href="#">All brewery events</a>
  <div class="hours">Hours of operation<br>Thursday - Friday: 4:00 PM - 8:00 PM<br>Saturday - 12:00 PM - 8:00 PM (Events 12:00 PM - 4:00 PM)<br>Sunday - 12:00 PM - 6:00 PM</div>
</section>
<div class="events-art" role="img" aria-label="Illustration of a seated figure with a staff and blue cape"></div>
<div class="rule" style="top:3050px"></div>

<div class="shop-art" role="img" aria-label="Illustration of a kneeling archer drawing a bow"></div>
<section class="shop">
  <h2 class="section-title">Our Shop</h2>
  <p>We brew up our passion for honest ingredients, our curiosity for different cultures, and social and environmental consciousness.</p>
  <div class="products">
    <div class="framed"><div class="product cap" role="img" aria-label="Blue cap"></div></div>
    <div class="framed"><div class="product tank" role="img" aria-label="Blue tank top"></div></div>
    <div class="framed"><div class="product growler" role="img" aria-label="Beer growler"></div></div>
  </div>
  <a class="btn" href="#">More merchandise</a>
</section>

<footer class="site-footer">
  <div class="footer-col" style="left:99px">
    <h5>7 Harbors Brewery</h5>
    <p>We brew up our passion for honest ingredients, our curiosity for different cultures, and social and environ mental consciousness into characteristic beers."</p>
    <p style="margin-top:12px">And "Beers with a Twist for the good of the world, for the fun of the party."</p>
  </div>
  <div class="footer-col" style="left:444px">
    <h5>Quick Links</h5>
    <ul class="links"><li>Home</li><li>Our Story</li><li>Brews</li><li>Blog</li><li>Events</li><li>Contact Us</li></ul>
  </div>
  <div class="footer-col" style="left:612px">
    <h5>Contact Us</h5>
    <div class="contact-item"><span class="ico"><svg viewBox="0 0 16 16"><path d="M8 1a5 5 0 0 1 5 5c0 4-5 9-5 9S3 10 3 6a5 5 0 0 1 5-5zm0 3a2 2 0 1 0 0 4 2 2 0 0 0 0-4z"/></svg></span><div><b>ADDRESS,</b>Building 1, Alder St<br>123 High Road London</div></div>
    <div class="contact-item"><span class="ico"><svg viewBox="0 0 16 16"><path d="M4 1h8v14H4z M6 12h4" fill="none" stroke="#c58c2b" stroke-width="1.8"/></svg></span><div><b>PHONE:</b>180 047 3918</div></div>
    <div class="contact-item"><span class="ico"><svg viewBox="0 0 16 16"><path d="M1 3h14v10H1z M1 3l7 6 7-6" fill="none" stroke="#c58c2b" stroke-width="1.8"/></svg></span><div><b>Mail:</b>info@7harborsbrewery.com</div></div>
  </div>
  <div class="footer-col newsletter" style="left:874px">
    <h5>Newsletter Signup</h5>
    <p style="margin-top:18px">Sign Up for our newsletter</p>
    <input type="text" placeholder="Email address" aria-label="Email address">
    <a class="btn" href="#">Subscribe</a>
  </div>
  <div class="footer-rule"></div>
  <div class="copyright">Copyright © 2017 7 Harbors Brewery. All Rights Reserved.</div>
  <div class="social" aria-label="Social links"><span></span><span></span><span></span><span></span><span></span></div>
</footer>

</body>
</html>
```